Consumer and commercial IOT solutions (Internet Of Things)

We are a startup and are looking for business cards with logo. The logo will appear on all of our media as well as our ecommerce site and social sites that have yet to be developed. We want to present a fresh face on a high tech company that innovates at every turn. You can read about our solutions on our information only web site www.plendacore.net - We have some wording we would like used on our business cards but there is no place for this except for here. The company name is "RM Industrial IOT" I have some samples of logos I am interested in seeing but I will let your team make the initial presentations

```html
<!DOCTYPE html>
<html lang="en">
<head>
<meta charset="utf-8">
<title>RM Industrial IOT – Business Card</title>
<link rel="stylesheet" href="https://fonts.googleapis.com/css2?family=Montserrat:wght@500;700&family=Roboto:wght@400&display=swap">
<style>
  :root {
    --brand-blue: #2a77c0;
    --ink-dark: #1e1f24;
    --ink-grey: #55585e;
    --paper: #f3f3f3;
    --backdrop: #e2e3e5;
    --edge: #1d5d8c;
  }
  * { box-sizing: border-box; margin: 0; padding: 0; }
  html, body { width: 1200px; height: 885px; overflow: hidden; }
  body {
    background: var(--backdrop);
    display: flex;
    flex-direction: column;
    align-items: center;
    justify-content: center;
    gap: 44px;
    font-family: "Roboto", sans-serif;
  }
  .card {
    width: 588px;
    height: 336px;
    position: relative;
    border-bottom: 3px solid var(--edge);
    box-shadow: 0 14px 28px rgba(0,0,0,0.12);
  }
  .card--front { background: var(--paper); }
  .card--back {
    background: var(--brand-blue);
    display: flex;
    align-items: center;
    justify-content: center;
  }
  .wordmark {
    font-family: "Montserrat", sans-serif;
    font-weight: 500;
    white-space: nowrap;
  }
  .card--front .wordmark {
    position: absolute;
    top: 56px;
    left: 0;
    right: 0;
    text-align: center;
    padding-left: 120px;
    color: var(--brand-blue);
    font-size: 24px;
  }
  .card--back .wordmark { color: #ffffff; font-size: 38px; }
  .divider {
    position: absolute;
    left: 216px;
    right: 38px;
    top: 161px;
    height: 1.5px;
    background: var(--brand-blue);
  }
  .person {
    position: absolute;
    left: 40px;
    top: 148px;
  }
  .person__name {
    font-family: "Montserrat", sans-serif;
    font-weight: 700;
    font-size: 18px;
    color: var(--ink-dark);
    letter-spacing: 0.02em;
    text-transform: uppercase;
  }
  .person__role {
    font-family: "Montserrat", sans-serif;
    font-weight: 500;
    font-size: 16px;
    color: var(--brand-blue);
    margin-top: 2px;
  }
  .contact {
    position: absolute;
    left: 56px;
    top: 222px;
    list-style: none;
    font-size: 15px;
    color: var(--ink-grey);
    line-height: 23px;
  }
  .contact li { display: flex; align-items: center; gap: 8px; }
  .contact svg { width: 13px; height: 13px; fill: var(--brand-blue); flex: none; }
  .address {
    position: absolute;
    right: 40px;
    top: 186px;
    text-align: right;
    font-size: 15px;
    line-height: 22px;
    color: var(--ink-grey);
    font-style: normal;
  }
  .address__company { color: var(--brand-blue); }
</style>
</head>
<body>
  <section class="card card--front" aria-label="Business card front">
    <div class="wordmark">RM Industrial IOT</div>
    <div class="divider"></div>
    <div class="person">
      <p class="person__name">Marcus Ellery</p>
      <p class="person__role">Founder &amp; CEO</p>
    </div>
    <ul class="contact">
      <li><svg viewBox="0 0 16 16" aria-hidden="true"><path d="M3.6 1.2l2.3 2.6-1.3 1.9c.9 2 2.6 3.7 4.6 4.7l1.9-1.3 2.6 2.3-1.4 2.4C6.7 13.5 2.3 9.2 1.2 3z"/></svg>555-014-2290</li>
      <li><svg viewBox="0 0 16 16" aria-hidden="true"><path d="M1 3h14v10H1z M2 4l6 5 6-5" fill="none" stroke="#2a77c0" stroke-width="1.6"/></svg>info@rmindustrialiot.com</li>
      <li><svg viewBox="0 0 16 16" aria-hidden="true"><circle cx="8" cy="8" r="6.3" fill="none" stroke="#2a77c0" stroke-width="1.5"/><path d="M1.7 8h12.6M8 1.7c-3 3.5-3 9.1 0 12.6M8 1.7c3 3.5 3 9.1 0 12.6" fill="none" stroke="#2a77c0" stroke-width="1.2"/></svg>www.rmindustrialiot.com</li>
    </ul>
    <address class="address">
      <span class="address__company">RM Industrial IOT</span><br>
      48 Harlow Creek Road<br>
      Maple Grove, ON L7B 3K2
    </address>
  </section>

  <section class="card card--back" aria-label="Business card back">
    <div class="wordmark">RM Industrial IOT</div>
  </section>
</body>
</html>
```